Core Investment Strategy's Super Pie Chart

We need a one page visual explanation of an investment strategy we call "Hollis/Varrowby". This strategy emphasizes a "core" portfolio that will seldom change and "perimeter" investments that will change. Our investment management firm caters to wealthy individuals. We want to project an image of strength and reliability. At the same time, we are willing to explore new concepts. I have uploaded a PDF of my graphically-challenged assistant's attempt at creating the one page visual.

Investment

```html
<!DOCTYPE html>
<html lang="en">
<head>
<meta charset="utf-8">
<title>Hollis/Varrowby Portfolio</title>
<link rel="stylesheet" href="https://fonts.googleapis.com/css2?family=Arimo:wght@700&display=swap">
<style>
  :root {
    --navy: #10284a;
    --navy-deep: #0a1a33;
    --orange: #f29222;
    --lime: #a6ce39;
    --blue: #0e6db6;
    --green: #8dc63f;
    --purple: #7b66a8;
    --crimson: #c8203f;
    --ink: #1c1c1c;
    --paper-light: #ffffff;
    --paper-edge: #d9d9db;
  }
  * { margin: 0; padding: 0; box-sizing: border-box; }
  html, body { width: 848px; height: 1200px; overflow: hidden; }
  body {
    position: relative;
    font-family: "Arimo", Arial, sans-serif;
    font-weight: 700;
    color: var(--ink);
    background: radial-gradient(ellipse at 50% 45%, var(--paper-light) 0%, #f1f1f2 55%, var(--paper-edge) 100%);
  }
  .band { position: absolute; left: 0; width: 848px; height: 70px; }
  .band--top { top: 0; }
  .band--bottom { bottom: 0; }
  .title {
    position: absolute; top: 106px; left: 0; width: 848px;
    text-align: center; font-size: 35px; letter-spacing: 0.5px; color: var(--ink);
  }
  .chart { position: absolute; left: 0; top: 0; width: 848px; height: 1200px; }
  .arc { filter: drop-shadow(3px 4px 4px rgba(0,0,0,0.28)); }
  .slice-label { fill: #fff; font-family: "Arimo", Arial, sans-serif; font-weight: 700; font-size: 15px; text-anchor: middle; }
  .slice-label--narrow { font-size: 13px; }
  .callout { position: absolute; display: flex; align-items: flex-start; gap: 11px; font-size: 17px; line-height: 23px; }
  .callout .swatch { width: 26px; height: 26px; flex: none; }
  .callout--other { left: 95px; top: 198px; }
  .callout--alt { left: 517px; top: 198px; }
  .callout--core { left: 96px; top: 826px; }
  .callout--active { left: 517px; top: 826px; }
  .legend { position: absolute; list-style: none; font-size: 23px; }
  .legend li { display: flex; align-items: center; gap: 14px; height: 37.5px; }
  .legend .dot { width: 11px; height: 11px; flex: none; }
  .legend--equities { left: 50px; top: 982px; }
  .legend--bonds { right: 38px; top: 982px; }
  .legend--bonds li { justify-content: flex-end; }
</style>
</head>
<body>
  <svg class="band band--top" viewBox="0 0 848 70" aria-hidden="true">
    <path d="M0 0 H848 V26 C640 44 420 60 0 64 Z" fill="var(--navy)"/>
    <path d="M0 64 C420 60 640 44 848 26" fill="none" stroke="var(--lime)" stroke-width="4"/>
    <path d="M0 70 C360 66 600 54 848 34" fill="none" stroke="var(--orange)" stroke-width="3"/>
  </svg>

  <h1 class="title">HOLLIS/VARROWBY PORTFOLIO</h1>

  <svg class="chart" viewBox="0 0 848 1200" aria-label="Portfolio allocation pie chart">
    <g class="arcs">
      <path class="arc" fill="var(--purple)" d="M350 248.9 A277 277 0 0 0 135.9 463 L162.6 463 A251 251 0 0 1 350 275.6 Z"/>
      <path class="arc" fill="var(--blue)" d="M464 248.9 A277 277 0 0 1 678.1 463 L651.4 463 A251 251 0 0 0 464 275.6 Z"/>
      <path class="arc" fill="var(--crimson)" d="M678.1 577 A277 277 0 0 1 464 791.1 L464 764.4 A251 251 0 0 0 651.4 577 Z"/>
      <path class="arc" fill="var(--green)" d="M350 791.1 A277 277 0 0 1 135.9 577 L162.6 577 A251 251 0 0 0 350 764.4 Z"/>
    </g>
    <g class="pie" stroke="#fff" stroke-width="4" stroke-linejoin="round">
      <path fill="var(--blue)" d="M407 520 L407 307 A213 213 0 0 1 557.6 670.6 Z"/>
      <path fill="var(--blue)" d="M407 520 L557.6 670.6 A213 213 0 0 1 486.8 717.5 Z"/>
      <path fill="var(--blue)" d="M407 520 L486.8 717.5 A213 213 0 0 1 407 733 Z"/>
      <path fill="var(--blue)" d="M407 520 L407 733 A213 213 0 0 1 259 673.2 Z"/>
      <path fill="var(--green)" d="M407 520 L259 673.2 A213 213 0 0 1 248.7 377.5 Z"/>
      <path fill="var(--green)" d="M407 520 L248.7 377.5 A213 213 0 0 1 407 307 Z"/>
    </g>
    <circle cx="407" cy="520" r="27" fill="#fff"/>
    <circle cx="407" cy="520" r="21" fill="#f2f2f2" stroke="#d6d6d6" stroke-width="1"/>

    <text class="slice-label" x="510" y="470">Lg. Cap<tspan x="510" dy="18">Equities,</tspan><tspan x="510" dy="18">30%</tspan></text>
    <text class="slice-label" x="341" y="379">Short-Term<tspan x="341" dy="18">Bonds,</tspan><tspan x="341" dy="18">10%</tspan></text>
    <text class="slice-label" x="297" y="506">Intermediate<tspan x="297" dy="18">Bonds,</tspan><tspan x="297" dy="18">20%</tspan></text>
    <text class="slice-label" x="349" y="625">Int'l/Dev.<tspan x="349" dy="18">Equities,</tspan><tspan x="349" dy="18">10%</tspan></text>
    <text class="slice-label slice-label--narrow" x="443" y="673">Sm.<tspan x="443" dy="15">Cap</tspan><tspan x="443" dy="15">Equities,</tspan><tspan x="443" dy="15">5%</tspan></text>
    <text class="slice-label slice-label--narrow" transform="translate(473 625) rotate(56.5)">Mid Cap Equities , 5%</text>
  </svg>

  <div class="callout callout--other"><span class="swatch" style="background:var(--purple)"></span><span>Other, 2%</span></div>
  <div class="callout callout--alt"><span class="swatch" style="background:var(--blue)"></span><span>Alternative Assets, 7%</span></div>
  <div class="callout callout--core"><span class="swatch" style="background:var(--green)"></span><span>Attractive Core Assets, 3%</span></div>
  <div class="callout callout--active"><span class="swatch" style="background:var(--crimson)"></span><span>Actively Managed Mutual<br>Funds, 8%</span></div>

  <ul class="legend legend--equities">
    <li><span class="dot" style="background:var(--blue)"></span>Lg. Cap Equities</li>
    <li><span class="dot" style="background:var(--blue)"></span>Mid Cap Equities</li>
    <li><span class="dot" style="background:var(--blue)"></span>Sm. Cap Equities</li>
    <li><span class="dot" style="background:var(--blue)"></span>Int'l/Dev. Equities</li>
  </ul>
  <ul class="legend legend--bonds">
    <li>Intermediate&nbsp; Bonds<span class="dot" style="background:var(--green)"></span></li>
    <li>Short-Term Bonds<span class="dot" style="background:var(--green)"></span></li>
  </ul>

  <svg class="band band--bottom" viewBox="0 0 848 70" aria-hidden="true">
    <path d="M0 70 H848 V14 C640 26 420 34 0 44 Z" fill="var(--navy-deep)"/>
    <path d="M0 44 C420 34 640 26 848 14" fill="none" stroke="var(--lime)" stroke-width="4"/>
    <path d="M0 36 C420 28 640 18 848 4" fill="none" stroke="var(--orange)" stroke-width="3"/>
  </svg>
</body>
</html>
```